Redesign of key pages of website

We have a website in development: (You can see the test version here: https://staging.pawvira.ai) We want a redesign of a) the home page, b) the set up screens (all four steps), c) the account home page, and the chat page (all four linked below). It needs to look amazing in both desktop and mobile. Also, the chat page needs to have a few different versions to give people a choice between them.

Four areas:
1) Home page: https://staging.pawvira.ai/
2) Account pages: https://staging.pawvira.ai/account/chatsettings.php?step=1
3) Account home page (you'll need to set up an account which is free): https://staging.pawvira.ai/account/summary.php
4) Chat page: https://staging.pawvira.ai/chat.php?id=375

Also to clarify re: code, I don't need any of the interaction/behavior code. I just need the basic HTML and stylesheets so I can integrate that into the existing website.

Please feel free to pass by early versions to me or if you have any clarifications, let me know!

Industry/Entity Type

small businesses

Coding

Coded - Design and coding required

Number of Pages Required

5+ page

Font styles to use
Other font styles liked:
• keep the current font.

Requirements
Must have
• All the same elements/functionality on the current site. Just want a redesign. Also keep the dog visual. Also must work great in mobile and desktop and be really fun and modern and easy.
Nice to have
• Also in the setup pages, need a much better form of navigation (currently just have four circles.)

```html
<!DOCTYPE html>
<html lang="en">
<head>
<meta charset="utf-8">
<title>Pawvira – Let Vira handle your leads</title>
<link rel="stylesheet" href="https://fonts.googleapis.com/css2?family=Josefin+Sans:wght@400;600;700&family=Roboto:wght@400;500;700&family=DM+Sans:wght@400;500;700&display=swap">
<style>
:root{
  --bg:#f3f7fe;
  --blue:#418cf5;
  --blue-deep:#2f78e0;
  --blue-dark:#0a5ce8;
  --blue-soft:#e8f0fd;
  --ink:#111318;
  --text:#2a2d33;
  --muted:#6d7480;
  --white:#ffffff;
  --footer:#3b3b3d;
  --send:#f2545b;
}
*{box-sizing:border-box;margin:0;padding:0}
html,body{width:1200px;height:2166px;overflow:hidden;background:var(--bg)}
body{position:relative;font-family:"Josefin Sans",sans-serif;color:var(--ink)}
.abs{position:absolute}

.brand{left:110px;top:20px;font-size:40px;font-weight:700;color:var(--blue);letter-spacing:-.5px}
.login-btn{left:886px;top:21px;width:200px;height:47px;border-radius:24px;background:var(--blue);color:var(--white);display:flex;align-items:center;justify-content:center;gap:9px;font-size:17px;font-weight:600}

.hero{left:110px;top:90px;width:978px;height:495px;border-radius:16px;background:var(--blue);overflow:hidden;box-shadow:0 14px 30px rgba(65,140,245,.18)}
.hero-wave{position:absolute;left:0;bottom:0}
.hero-title{position:absolute;left:52px;top:112px;font-size:48px;font-weight:700;color:var(--white)}
.hero-lead{position:absolute;left:53px;top:174px;width:420px;font-size:32px;line-height:51px;color:var(--white);letter-spacing:.6px}
.mascot{position:absolute;border-radius:50% 46% 48% 52%;background:radial-gradient(circle at 50% 45%,#8ea6f7 0 34%,#ffffff 35%)}
.hero .mascot{left:520px;top:45px;width:405px;height:390px}

.feature-title{font-size:35px;font-weight:700;letter-spacing:.3px}
.feature-title span{color:var(--blue)}
.feature-text{font-size:15px;line-height:26px;color:var(--text);letter-spacing:.3px}
.feature-text p+p{margin-top:25px}

.card{background:var(--white);border-radius:14px;box-shadow:7px 7px 0 var(--blue),0 4px 14px rgba(0,0,0,.06)}

.chat-card{left:665px;top:662px;width:342px;height:256px;font-family:"Roboto",sans-serif}
.biz-logo{position:absolute;left:30px;top:28px;width:52px;height:52px;border-radius:50%;border:2px solid #f08a3c}
.biz-name{position:absolute;left:103px;top:30px;font-size:16px;font-weight:500;color:#333}
.biz-role{position:absolute;left:103px;top:52px;font-size:11px;color:#666}
.socials{position:absolute;left:104px;top:73px;display:flex;gap:20px}
.socials i{width:20px;height:20px;border-radius:50%;background:#3a3d45;display:block}
.bot-avatar{position:absolute;left:32px;top:115px;width:62px;height:62px;border-radius:50%;background:radial-gradient(circle,#7b9cf5,#c8d3fb)}
.bot-msg{position:absolute;left:113px;top:132px;font-size:13.5px;line-height:17px;color:#333}
.msg-input{position:absolute;left:16px;top:213px;width:300px;height:30px;background:#f3f4f6;border-radius:4px;font-size:13px;color:#9aa0a8;padding:7px 10px}
.send-btn{position:absolute;left:265px;top:208px;width:40px;height:40px;border-radius:50%;background:var(--send);display:flex;align-items:center;justify-content:center}

.cal-card{left:107px;top:992px;width:502px;height:305px;font-family:"DM Sans",sans-serif;box-shadow:-6px -6px 0 var(--blue),0 4px 14px rgba(0,0,0,.06)}
.cal-title{position:absolute;left:20px;top:15px;font-size:17px;font-weight:700}
.cal-nav{position:absolute;top:44px;width:35px;height:35px;border-radius:50%;background:var(--blue-soft);display:flex;align-items:center;justify-content:center}
.cal-month{position:absolute;left:142px;top:53px;font-size:14px;color:#333}
.cal-grid{position:absolute;left:10px;top:98px;display:grid;grid-template-columns:repeat(7,49px);row-gap:8px}
.cal-grid .dow{font-size:10.5px;color:#333;text-align:center;height:25px}
.cal-grid .d{width:40px;height:40px;margin:0 auto;border-radius:50%;display:flex;align-items:center;justify-content:center;font-size:13px;color:#666}
.cal-grid .on{background:var(--blue-soft);color:var(--blue-dark);font-weight:700}
.cal-grid .sel{background:var(--blue-dark);color:var(--white);font-weight:700}
.slot{position:absolute;left:360px;width:126px;height:48px;border:1.5px solid #9ec1f7;border-radius:3px;display:flex;align-items:center;justify-content:center;font-size:14px;font-weight:700;color:var(--blue-dark)}

.table-card{left:523px;top:1389px;width:557px;height:259px;font-family:"Roboto",sans-serif}
.leads{position:absolute;left:16px;top:16px;width:529px;border-collapse:collapse;font-size:14px;color:#333}
.leads th{background:#1f86e2;color:var(--white);text-align:left;height:38px;padding:0 17px;font-weight:700;font-size:15px;border:1px solid #1a6ec0}
.leads td{border:1px solid #c9ccd2;vertical-align:middle;padding:8px 10px;line-height:18.5px}
.leads ul{padding-left:26px}

.cta{left:0;top:1750px;width:1200px;height:345px;background:linear-gradient(135deg,#3a86ee,#4a93f6)}
.cta .mascot{left:126px;top:36px;width:286px;height:272px}
.cta-title{position:absolute;left:507px;top:110px;font-size:35px;color:var(--white);letter-spacing:.6px}
.cta-btn{position:absolute;left:509px;top:179px;width:272px;height:51px;border-radius:26px;background:var(--white);color:var(--blue);font-size:22px;font-weight:600;display:flex;align-items:center;justify-content:center;letter-spacing:.5px}

.site-footer{left:0;top:2095px;width:1200px;height:71px;background:var(--footer);color:var(--white);font-size:16px;font-weight:600;display:flex;align-items:center;justify-content:center}
</style>
</head>
<body>

<header>
  <div class="abs brand">Pawvira</div>
  <a class="abs login-btn">
    <svg width="24" height="24" viewBox="0 0 24 24" fill="none" stroke="#fff" stroke-width="1.8"><path d="M13 3h7v18h-7M3 12h12M11 8l4 4-4 4"/></svg>
    Login or Register
  </a>
</header>

<section class="abs hero">
  <svg class="hero-wave" width="978" height="110" viewBox="0 0 978 110"><path d="M0 20 C120 0 220 60 330 50 C460 40 520 10 640 40 C760 70 860 30 978 60 V110 H0Z" fill="#3179de"/></svg>
  <h1 class="hero-title">Welcome!</h1>
  <p class="hero-lead">Vira talks to your leads, qualifies them, and gets them on your calendar.</p>
  <div class="mascot" role="img" aria-label="Illustration of the blue puppy mascot Vira"></div>
</section>

<section>
  <h2 class="abs feature-title" style="left:183px;top:710px">Customize and <span>share</span></h2>
  <div class="abs feature-text" style="left:184px;top:762px;width:420px">
    <p>Customize the appearance, conversation, and much more.</p>
    <p>You can then share Vira by embedding it in your website or via a personalized link</p>
  </div>
  <div class="abs card chat-card">
    <div class="biz-logo"></div>
    <div class="biz-name">Maren Studio</div>
    <div class="biz-role">Hairdresser/Stylist</div>
    <div class="socials"><i></i><i></i><i></i><i></i></div>
    <div class="bot-avatar" role="img" aria-label="Small puppy mascot avatar"></div>
    <p class="bot-msg">Hi! I'm Vira, Maren's assistant.<br>How did you hear about Maren?</p>
    <div class="msg-input">Enter your message..</div>
    <div class="send-btn"><svg width="18" height="18" viewBox="0 0 24 24" fill="none" stroke="#fff" stroke-width="2"><path d="M22 2L11 13M22 2l-7 20-4-9-9-4z"/></svg></div>
  </div>
</section>

<section>
  <div class="abs card cal-card">
    <div class="cal-title">Select a Date &amp; Time</div>
    <div class="cal-nav" style="left:76px"><svg width="12" height="12" viewBox="0 0 12 12" fill="none" stroke="#0a5ce8" stroke-width="2"><path d="M8 2L4 6l4 4"/></svg></div>
    <div class="cal-month">June 2023</div>
    <div class="cal-nav" style="left:244px"><svg width="12" height="12" viewBox="0 0 12 12" fill="none" stroke="#0a5ce8" stroke-width="2"><path d="M4 2l4 4-4 4"/></svg></div>
    <div class="cal-grid">
      <div class="dow">SUN</div><div class="dow">MON</div><div class="dow">TUE</div><div class="dow">WED</div><div class="dow">THU</div><div class="dow">FRI</div><div class="dow">SAT</div>
      <div></div><div></div><div></div><div></div><div class="d on">1</div><div class="d on">2</div><div class="d">3</div>
      <div class="d">4</div><div class="d on">5</div><div class="d on">6</div><div class="d on">7</div><div class="d on">8</div><div class="d on">9</div><div class="d">10</div>
      <div class="d">11</div><div class="d on">12</div><div class="d sel">13</div><div class="d on">14</div><div class="d on">15</div><div class="d on">16</div><div class="d">17</div>
    </div>
    <div class="slot" style="top:97px">10:00am</div>
    <div class="slot" style="top:154px">10:30am</div>
    <div class="slot" style="top:211px">11:00am</div>
  </div>
  <h2 class="abs feature-title" style="left:667px;top:1063px">Qualify and <span>schedule</span></h2>
  <div class="abs feature-text" style="left:668px;top:1114px;width:400px">
    <p>Get the information you need from your customers.</p>
    <p>After they meet your criteria, they can book a meeting directly on your calendar.</p>
  </div>
</section>

<section>
  <h2 class="abs feature-title" style="left:111px;top:1443px">Manage your <span>leads</span></h2>
  <div class="abs feature-text" style="left:111px;top:1495px;width:390px">
    <p>Get notified via email or text.</p>
    <p>See a summary of each lead and manage them in one place. Search, sort, add notes, and more.</p>
  </div>
  <div class="abs card table-card">
    <table class="leads">
      <thead><tr><th style="width:353px">summary</th><th>email</th></tr></thead>
      <tbody>
        <tr style="height:92px"><td><ul><li>Interested in a fitness coach</li><li>Does not currently work out</li><li>Specifically interested in arms and strength</li><li>In the Seattle area and flexible on time</li></ul></td><td>dan.keller@mailbox.test</td></tr>
        <tr style="height:102px"><td><ul><li>Interested in a new fitness coach</li><li>Works out 3 times a week</li><li>Has a fitness instructor now but his approach is too relaxed</li></ul></td><td>lena.moor@mailbox.test</td></tr>
      </tbody>
    </table>
  </div>
</section>

<section class="abs cta">
  <div class="mascot" role="img" aria-label="Illustration of the blue puppy mascot Vira"></div>
  <h2 class="cta-title">Let Vira handle your leads today!</h2>
  <a class="cta-btn">Create your Vira now!</a>
</section>

<footer class="abs site-footer">Copyrights@2023.pawvira.All Rights Reserved</footer>

</body>
</html>
```